New packaging company website**

We are looking for a new design for our corporate website (www.cratevendo.it). The theme must be made with Elementor and Crocoblock plugins. Currently the demo site can be reached at www.cratevendo.cloud

You can also check our current site for your reference www.cratevendo.it
We mainly deal with the resale of industrial containers for companies, most of our customers are B2B but also a good number of private customers. The site must therefore be accessible to all and the prices always visible even without registration or other.

Given the heterogeneity of our articles, we need a very clear shop page, with clearly visible filters and possibly with a list view and a table.

However, it does not have to be a simple ecommerce, we still want a site with many texts, spaces for product FAQs, tooltips on filters or attributes.

Target Market(s)

90% B2B

Coding

Coded - Design and coding required

Requirements
Must have
• beautiful, modern and captivating graphics. It must be a "full" site and not a flat one.
Nice to have
• We are undecided about the location of the main product menu.

If you leave the top bar with the icons and labels of the macro categories, as happens now on the live site and on the demo site.

Or if you want to insert the classic "all categories" on the top menu (https://lumberfay.qrivenso.com/demo-tools/demo/tools/ or https://www.havelintheme.com/wordpress/havel/shop30/)

Or if you want to take advantage of something more modern, such as the sidebar menu (https://www.havelintheme.com/wordpress/havel/shop10/ or https://www.havelintheme.com/wordpress/havel/shop19/)

```html
<!DOCTYPE html>
<html lang="it">
<head>
<meta charset="utf-8">
<title>Cratevendo – Forniture per enti e aziende</title>
<link href="https://fonts.googleapis.com/css2?family=Poppins:wght@300;400;500;600;700;800;900&display=swap" rel="stylesheet">
<style>
:root{
  --blue:#1c5ea7;
  --blue-dark:#164d8c;
  --yellow:#ffd600;
  --ink:#222529;
  --text:#555a60;
  --muted:#8a8f95;
  --line:#e6e7e9;
  --soft:#f3f4f5;
  --white:#fff;
}
*{box-sizing:border-box;margin:0;padding:0}
html,body{width:1200px;height:3986px;overflow:hidden}
body{font-family:'Poppins',sans-serif;color:var(--ink);background:var(--white);position:relative}
a{color:inherit;text-decoration:none}

/* top bar */
.topbar{position:absolute;left:0;top:0;width:1200px;height:36px;border-bottom:1px solid var(--line);font-size:12px;font-weight:500}
.topbar .phone-box{position:absolute;left:88px;top:0;width:36px;height:36px;background:var(--yellow);display:flex;align-items:center;justify-content:center}
.topbar .assist{position:absolute;left:136px;top:9px;font-weight:600}
.topbar .links{position:absolute;right:90px;top:9px;display:flex;gap:22px;color:#333}
.topbar .links span{display:flex;align-items:center;gap:6px}

/* header */
.header{position:absolute;left:0;top:36px;width:1200px;height:97px}
.brand{position:absolute;display:flex;align-items:center;gap:10px;color:var(--blue);font-weight:800;letter-spacing:.5px}
.brand .mark{background:var(--blue);display:block}
.search{position:absolute;left:398px;top:29px;width:376px;height:37px;border:1px solid var(--line);display:flex;font-size:11px;color:var(--muted)}
.search .field{flex:1;padding:11px 12px}
.search .cat{width:134px;border-left:1px solid var(--line);padding:11px 12px;font-size:10px;text-transform:uppercase}
.search .go{width:41px;background:var(--yellow);display:flex;align-items:center;justify-content:center}
.account{position:absolute;left:801px;top:38px;font-size:14px;font-weight:500;display:flex;align-items:center;gap:8px}
.hdr-icon{position:absolute;top:36px}
.badge{position:absolute;top:-6px;right:-8px;width:14px;height:14px;border-radius:50%;background:var(--yellow);font-size:9px;font-weight:600;display:flex;align-items:center;justify-content:center}
.cart-total{position:absolute;left:1070px;top:40px;font-size:14px;font-weight:600}

/* hero */
.sidebar{position:absolute;left:0;top:133px;width:88px;height:501px;background:var(--blue)}
.sidebar svg{position:absolute;left:29px}
.sidebar .more{position:absolute;left:0;width:88px;top:452px;text-align:center;color:var(--yellow);font-weight:700;font-size:15px;text-decoration:underline}
.hero{position:absolute;left:88px;top:133px;width:1112px;height:501px;background:linear-gradient(90deg,#f1f2f3,#eceef0)}
.hero h1{position:absolute;left:84px;top:130px;font-size:54px;line-height:50px;font-weight:800;color:var(--ink);letter-spacing:1px}
.hero .sub{position:absolute;left:84px;top:242px;font-size:17px;font-weight:500;letter-spacing:.5px}
.hero .small{position:absolute;left:84px;top:282px;font-size:14px;color:var(--text)}
.btn-yellow{background:var(--yellow);font-weight:700;font-size:14px;display:flex;align-items:center;gap:8px;justify-content:center}
.hero .btn-yellow{position:absolute;left:84px;top:320px;width:201px;height:45px}
.hero .lockers{position:absolute;left:518px;top:115px;width:494px;height:386px;
  background:
   radial-gradient(ellipse 60% 50% at 45% 40%,rgba(255,255,255,.9),transparent 70%),
   linear-gradient(90deg,#e9ebee 0%,#f8f9fa 35%,#e4e7ea 70%,#cfd3d7 100%);
  box-shadow:-20px 0 40px rgba(0,0,0,.04)}
.arrow{position:absolute;top:240px}

/* about */
.about h2{position:absolute;left:88px;top:832px;font-size:36px;font-weight:800;letter-spacing:1px}
.about h3{position:absolute;left:88px;top:882px;font-size:16px;font-weight:600;letter-spacing:.3px}
.about p{position:absolute;left:88px;top:920px;width:490px;font-size:15px;line-height:23px;color:var(--text)}
.about .tel{position:absolute;left:88px;top:1058px;display:flex;align-items:center;gap:14px;font-size:20px;font-weight:600;color:var(--blue)}
.about .tel span{border-bottom:2px solid var(--blue)}
.about .deco{position:absolute;left:766px;top:722px;width:343px;height:344px;background:var(--yellow)}
.about .dots{position:absolute;left:946px;top:742px;width:140px;height:190px;background-image:radial-gradient(#b58f00 1.2px,transparent 1.6px);background-size:9px 9px;opacity:.7}
.about .photo{position:absolute;left:631px;top:776px;width:424px;height:376px;
  background:
   radial-gradient(ellipse 22% 45% at 52% 50%,#7d8088 0%,rgba(125,128,136,.5) 55%,transparent 100%),
   radial-gradient(ellipse 40% 60% at 90% 40%,#a8562e 0%,transparent 75%),
   linear-gradient(100deg,#b8a996 0%,#d8d2ca 40%,#9b958d 75%,#5f5a55 100%)}

/* sections */
.sec-title{position:absolute;left:88px;font-size:19px;font-weight:600;letter-spacing:.5px}
.view-all{position:absolute;left:1002px;width:108px;height:36px;background:#2b2d30;color:#fff;font-size:11px;font-weight:700;display:flex;align-items:center;justify-content:center}
.products{position:absolute;left:88px;width:1022px;display:flex;gap:16px}
.card{width:192px}
.card .pic{height:209px;background:
  radial-gradient(ellipse 38% 30% at 50% 48%,var(--tone) 0%,var(--tone) 45%,transparent 100%),
  radial-gradient(ellipse 45% 12% at 50% 78%,rgba(0,0,0,.10),transparent 100%),
  var(--soft)}
.card .name{margin-top:15px;height:48px;padding-right:8px;font-size:11px;line-height:16px;text-transform:uppercase;color:#333;overflow:hidden}
.card .stars{margin-top:12px;height:13px;width:78px;background:radial-gradient(circle,#d9dadc 5px,transparent 5.5px) 0 0/16px 13px repeat-x}
.card .price{margin-top:10px;position:relative;padding-left:24px;font-size:17px;font-weight:600}
.card .price::before{content:"\2661";position:absolute;left:0;top:0;font-size:16px;color:#888;font-weight:400}

/* promo banners */
.promo{position:absolute;overflow:visible}
.deals{left:88px;top:1722px;width:492px;height:184px;background:#eeeeee}
.deals .k{position:absolute;left:36px;top:38px;font-size:15px;font-weight:500;letter-spacing:.5px}
.deals .big{position:absolute;left:34px;top:56px;font-size:52px;font-weight:800;letter-spacing:1px}
.deals .up{position:absolute;left:88px;top:118px;display:flex;align-items:center;gap:8px;font-size:11px;font-weight:600}
.deals .up b{background:var(--blue);color:#fff;font-size:19px;padding:1px 9px}
.deals .pic{position:absolute;left:250px;top:30px;width:240px;height:180px;background:
  radial-gradient(ellipse 30% 38% at 38% 58%,#2d8fe3 0%,#2d8fe3 55%,transparent 100%),
  radial-gradient(ellipse 26% 30% at 70% 62%,#e4e8eb 0%,#d3d8dc 55%,transparent 100%),
  radial-gradient(ellipse 16% 24% at 48% 26%,#3aa0e8 0%,#3aa0e8 50%,transparent 100%)}
.tools{left:619px;top:1722px;width:491px;height:184px;background:linear-gradient(90deg,#1b5b9c,#2a7cc0)}
.tools .k{position:absolute;left:43px;top:38px;color:#fff;font-size:14px;font-weight:600;letter-spacing:.5px}
.tools .rule{position:absolute;left:46px;top:105px;width:78px;height:2px;background:#fff}
.tools .pct{position:absolute;left:136px;top:58px;font-size:52px;line-height:52px;font-weight:800;color:var(--yellow)}
.tools .off{position:absolute;left:136px;top:106px;font-size:52px;line-height:52px;font-weight:800;color:#fff}
.tools .pic{position:absolute;left:276px;top:20px;width:180px;height:225px;background:
  radial-gradient(ellipse 38% 30% at 50% 30%,#55595f 0%,#55595f 50%,transparent 100%),
  radial-gradient(ellipse 42% 30% at 50% 68%,#ef8a1c 0%,#ef8a1c 50%,transparent 100%)}

.sale{left:88px;top:2490px;width:492px;height:186px;background:var(--yellow)}
.sale .k{position:absolute;left:36px;top:44px;font-size:13px;font-weight:600}
.sale .big{position:absolute;left:35px;top:62px;font-size:40px;font-weight:800;letter-spacing:.5px}
.sale .btn{position:absolute;left:36px;top:112px;width:170px;height:37px;background:#2b2d30;color:#fff;font-size:13px;font-weight:700;display:flex;align-items:center;justify-content:center;gap:8px}
.sale .fifty{position:absolute;left:282px;top:8px;font-size:150px;line-height:170px;font-weight:900;letter-spacing:-4px;color:#2b2d30}
.sale .pc{position:absolute;left:417px;top:84px;font-size:12px;font-weight:800;line-height:13px;color:var(--yellow);text-align:center}
.coll{left:619px;top:2490px;width:491px;height:186px;background-color:#f1f2f3;background-image:radial-gradient(#dcdee0 1px,transparent 1.2px);background-size:8px 8px}
.coll .k{position:absolute;left:0;width:358px;text-align:center;top:44px;font-size:13px;font-weight:600}
.coll .big{position:absolute;left:0;width:358px;text-align:center;top:58px;font-size:45px;font-weight:800}
.coll .rule{position:absolute;left:34px;width:290px;top:120px;height:1px;background:#cfd2d5}
.coll .s{position:absolute;left:0;width:358px;text-align:center;top:130px;font-size:13px;color:#444}
.coll .pic{position:absolute;left:262px;top:80px;width:210px;height:140px;background:
  radial-gradient(ellipse 32% 40% at 45% 40%,#f26b1d 0%,#f26b1d 50%,transparent 100%),
  radial-gradient(ellipse 26% 30% at 78% 45%,#f3c21b 0%,#f3c21b 45%,transparent 100%),
  radial-gradient(ellipse 40% 18% at 45% 78%,#e9b325 0%,rgba(233,179,37,.6) 50%,transparent 100%)}

/* features */
.features{position:absolute;left:88px;top:3295px;width:1022px;height:90px}
.feat{position:absolute;top:0;display:flex;gap:15px}
.feat .ic{width:84px;height:84px;border-radius:50%;background:var(--soft);display:flex;align-items:center;justify-content:center;flex:none}
.feat h4{font-size:12px;font-weight:700;line-height:14px;margin-top:12px;text-transform:uppercase}
.feat p{font-size:12px;line-height:15px;color:var(--muted);margin-top:6px}

/* newsletter */
.news{position:absolute;left:0;top:3440px;width:1200px;height:168px;background:var(--blue);color:#fff}
.news .k{position:absolute;left:88px;top:42px;font-size:16px;font-weight:700}
.news .big{position:absolute;left:86px;top:54px;font-size:43px;font-weight:800;letter-spacing:1.5px}
.news .s{position:absolute;left:88px;top:115px;font-size:12px;font-weight:500}
.news .field{position:absolute;left:626px;top:59px;width:372px;height:51px;background:#fff;color:var(--muted);font-size:13px;display:flex;align-items:center;gap:10px;padding-left:24px}
.news .btn{position:absolute;left:998px;top:59px;width:112px;height:51px;background:var(--yellow);color:var(--ink);font-size:14px;font-weight:700;display:flex;align-items:center;justify-content:center}

/* footer */
.foot-col{position:absolute;top:3674px}
.foot-col h5{font-size:14px;font-weight:600;letter-spacing:.5px;margin-bottom:20px}
.foot-col li{list-style:none;font-size:13px;color:var(--text);line-height:18px;margin-bottom:9px}
.social{position:absolute;top:3798px;width:30px;height:30px;border-radius:50%;background:#eceeef}
.paycard{position:absolute;width:43px;height:25px;border-radius:3px}
.copy-line{position:absolute;left:88px;top:3909px;width:1022px;height:1px;background:var(--line)}
.copy{position:absolute;left:0;width:1200px;top:3950px;text-align:center;font-size:11px;font-weight:600;letter-spacing:.3px}
.totop{position:absolute;left:1130px;top:3908px;width:44px;height:44px;border-radius:50%;background:var(--yellow);display:flex;align-items:center;justify-content:center}
</style>
</head>
<body>

<div class="topbar">
  <div class="phone-box"><svg width="14" height="14" viewBox="0 0 24 24"><path d="M6.6 10.8a15 15 0 0 0 6.6 6.6l2.2-2.2c.3-.3.7-.4 1-.2 1.1.4 2.3.6 3.6.6.6 0 1 .4 1 1V20c0 .6-.4 1-1 1A17 17 0 0 1 3 4c0-.6.4-1 1-1h3.5c.6 0 1 .4 1 1 0 1.3.2 2.5.6 3.6.1.3 0 .7-.2 1z" fill="#222"/></svg></div>
  <div class="assist">ASSISTENZA 02/55510420</div>
  <div class="links">
    <span><svg width="16" height="12" viewBox="0 0 16 12"><rect x="0" y="1" width="10" height="7" fill="#777"/><path d="M10 3h3l3 3v2h-6z" fill="#777"/><circle cx="4" cy="10" r="1.6" fill="#777"/><circle cx="12" cy="10" r="1.6" fill="#777"/></svg>Spedizioni in tutta Italia</span>
    <span><svg width="14" height="14" viewBox="0 0 14 14"><path d="M7 1l6 3v6l-6 3-6-3V4z" fill="#777"/></svg>Preventivo GRATUITO</span>
    <span><svg width="14" height="14" viewBox="0 0 14 14"><circle cx="7" cy="7" r="4" fill="#777"/><g stroke="#777" stroke-width="1.2"><path d="M7 0v3M7 11v3M0 7h3M11 7h3M2 2l2 2M10 10l2 2M12 2l-2 2M4 10l-2 2"/></g></svg>Prodotti COVID-19</span>
  </div>
</div>

<div class="header">
  <div class="brand" style="left:88px;top:26px;font-size:27px"><span class="mark" style="width:28px;height:28px"></span>CRATEVENDO</div>
  <div class="search">
    <div class="field">Search for products</div>
    <div class="cat">Select category &#8964;</div>
    <div class="go"><svg width="16" height="16" viewBox="0 0 16 16"><circle cx="6.5" cy="6.5" r="5" fill="none" stroke="#222" stroke-width="1.6"/><path d="M10.5 10.5l4 4" stroke="#222" stroke-width="1.8"/></svg></div>
  </div>
  <div class="account"><svg width="20" height="20" viewBox="0 0 20 20"><circle cx="10" cy="6" r="4" fill="none" stroke="#222" stroke-width="1.5"/><path d="M2 19c1-5 4-7 8-7s7 2 8 7" fill="none" stroke="#222" stroke-width="1.5"/></svg>Accedi / Registrati</div>
  <div class="hdr-icon" style="left:985px"><svg width="22" height="20" viewBox="0 0 24 22"><path d="M12 20S2 13.5 2 7.3A5 5 0 0 1 12 5a5 5 0 0 1 10 2.3C22 13.5 12 20 12 20z" fill="none" stroke="#222" stroke-width="1.6"/></svg><span class="badge">0</span></div>
  <div class="hdr-icon" style="left:1033px"><svg width="22" height="20" viewBox="0 0 24 22"><path d="M1 2h4l3 12h12l3-9H7" fill="none" stroke="#222" stroke-width="1.6"/><circle cx="9" cy="19" r="1.7" fill="#222"/><circle cx="19" cy="19" r="1.7" fill="#222"/></svg><span class="badge">0</span></div>
  <div class="cart-total">$0.00</div>
</div>

<div class="sidebar">
  <svg style="top:27px" width="30" height="30" viewBox="0 0 30 30" fill="none" stroke="#fff" stroke-width="1.6"><rect x="5" y="7" width="20" height="21" rx="2"/><path d="M10 2h10v5H10zM10 14h10M10 20h10"/></svg>
  <svg style="top:99px" width="30" height="30" viewBox="0 0 30 30" fill="none" stroke="#fff" stroke-width="1.6"><ellipse cx="15" cy="6" rx="10" ry="3"/><path d="M5 6v18c0 2 4.5 3 10 3s10-1 10-3V6M5 15c0 2 4.5 3 10 3s10-1 10-3"/></svg>
  <svg style="top:172px" width="30" height="30" viewBox="0 0 30 30" fill="none" stroke="#fff" stroke-width="1.6"><path d="M4 7h22M11 7V3h8v4M7 7l2 21h12l2-21M12 11v13M18 11v13"/></svg>
  <svg style="top:243px" width="30" height="30" viewBox="0 0 30 30" fill="none" stroke="#fff" stroke-width="1.6"><rect x="3" y="3" width="24" height="24"/><path d="M3 11h24M3 19h24M10 3v8M20 11v8M10 19v8"/></svg>
  <svg style="top:313px" width="30" height="30" viewBox="0 0 30 30" fill="none" stroke="#fff" stroke-width="1.6"><rect x="5" y="4" width="20" height="20"/><path d="M5 14h20M15 4v20M3 28h24M8 24v4M22 24v4"/></svg>
  <svg style="top:386px" width="30" height="30" viewBox="0 0 30 30" fill="none" stroke="#fff" stroke-width="1.6"><rect x="4" y="8" width="16" height="20"/><path d="M8 13h3M13 13h3M8 18h3M13 18h3M10 28v-5h4v5"/><circle cx="23" cy="7" r="5"/><path d="M23 4v6M20 7h6"/></svg>
  <div class="more">MORE</div>
</div>
<div class="hero">
  <div class="lockers" role="img" aria-label="Fila di armadietti spogliatoio in metallo grigio chiaro"></div>
  <svg class="arrow" style="left:38px" width="14" height="20" viewBox="0 0 14 20"><path d="M11 2L3 10l8 8" fill="none" stroke="#b7bbbf" stroke-width="2"/></svg>
  <svg class="arrow" style="left:1060px" width="14" height="20" viewBox="0 0 14 20"><path d="M3 2l8 8-8 8" fill="none" stroke="#b7bbbf" stroke-width="2"/></svg>
  <h1>ARMADI<br>SPOGLIATOIO</h1>
  <div class="sub">SALVASPAZIO, TRADIZIONALI, SPORCO PULITO</div>
  <div class="small">Scrpri la vasta gamma di armadietti in metallo</div>
  <div class="btn-yellow"><svg width="16" height="14" viewBox="0 0 16 14"><path d="M1 5h14l-2 8H3zM5 5l3-4 3 4" fill="#222"/></svg>ACQUISTA ORA!</div>
</div>

<section class="about">
  <div class="deco"></div>
  <div class="dots"></div>
  <div class="photo" role="img" aria-label="Magazziniere con tablet accanto a un transpallet in un magazzino con scaffali"></div>
  <h2>CRATEVENDO</h2>
  <h3>VENDITA ONLINE FORNITURE PER ENTI E AZIENDE</h3>
  <p>Contenitori In Plastica, Contenitori in Metallo, Scaffali, Armadietti, Sicurezza &amp; Ambiente, Pallet E Bancali, prodotti per l'imballaggio, Pronto Soccorso, Antinfortunistica e DPI Consegna in 24/48H in tutta Italia. Prodotti al miglior prezzo, per il buon funzionamento di ogni ente e impresa.</p>
  <div class="tel"><svg width="24" height="24" viewBox="0 0 24 24"><path d="M6.6 10.8a15 15 0 0 0 6.6 6.6l2.2-2.2c.3-.3.7-.4 1-.2 1.1.4 2.3.6 3.6.6.6 0 1 .4 1 1V20c0 .6-.4 1-1 1A17 17 0 0 1 3 4c0-.6.4-1 1-1h3.5c.6 0 1 .4 1 1 0 1.3.2 2.5.6 3.6.1.3 0 .7-.2 1z" fill="#f4c400"/></svg><span>02/55510420</span></div>
</section>

<div class="sec-title" style="top:1248px">CONTENITORI IN METALLO</div>
<div class="view-all" style="top:1242px">VIEW ALL</div>
<div class="products" style="top:1307px">
  <div class="card"><div class="pic" style="--tone:#f0671e" role="img" aria-label="Benna ribaltabile arancione in acciaio"></div><div class="name">Steel tipper and fork buckets, forklift loading, without wheels</div><div class="stars"></div><div class="price">€676.37</div></div>
  <div class="card"><div class="pic" style="--tone:#5d6b43" role="img" aria-label="Taniche per carburante in metallo verde"></div><div class="name">Metal petrol cans, ADR / ONU approved, green color</div><div class="stars"></div><div class="price">€23.45</div></div>
  <div class="card"><div class="pic" style="--tone:#d9dcdf" role="img" aria-label="Barattoli in metallo vuoti con coperchio a pressione"></div><div class="name">Empty metal cans with pressure lid ideal for paints, chemistry</div><div class="stars"></div><div class="price">€0.83</div></div>
  <div class="card"><div class="pic" style="--tone:#cdb896" role="img" aria-label="Coperchio con cerchio in metallo per secchi"></div><div class="name">Lids with metal tie for metal buckets, lacquered color</div><div class="stars"></div><div class="price">€1.99</div></div>
  <div class="card"><div class="pic" style="--tone:#e9662a" role="img" aria-label="Contenitori metallici arancioni a fondo apribile"></div><div class="name">Contenitori metallici a fondo apribile, fondello doppio...</div><div class="stars"></div><div class="price">€628,34</div></div>
</div>

<div class="promo deals">
  <div class="pic" role="img" aria-label="Serbatoi e cisterne in plastica blu e bianca"></div>
  <div class="k">CONTENITORI IN PLASTICA</div>
  <div class="big">DEALS</div>
  <div class="up">UP TO <b>$100</b> OFF</div>
</div>
<div class="promo tools">
  <div class="pic" role="img" aria-label="Carrello porta attrezzi arancione con cassetti e utensili"></div>
  <div class="k">TORVA UTENSILI E ATTREZZI</div>
  <div class="rule"></div>
  <div class="pct">50%</div>
  <div class="off">OFF</div>
</div>

<div class="sec-title" style="top:2027px">ANTINFORTUNISTICA E DPI</div>
<div class="view-all" style="top:2013px">VIEW ALL</div>
<div class="products" style="top:2077px">
  <div class="card"><div class="pic" style="--tone:#f2c52a" role="img" aria-label="Guanti da lavoro gialli in nitrile"></div><div class="name">Guanti da lavoro in jersey impregnato di nitrile leggero...</div><div class="stars"></div><div class="price">€0,76</div></div>
  <div class="card"><div class="pic" style="--tone:#3c3d40" role="img" aria-label="Scarpa antinfortunistica alta in pelle nera"></div><div class="name">Scarpe antinfortunistiche da lavoro, S1P SRC, alte, in crosta bovina...</div><div class="stars"></div><div class="price">€24,84</div></div>
  <div class="card"><div class="pic" style="--tone:#ee7a1f" role="img" aria-label="Cuffie antirumore arancioni"></div><div class="name">Cuffie antirumore ad archetto ruotabile, attenuazione in dB 27 SN...</div><div class="stars"></div><div class="price">€5,81</div></div>
  <div class="card"><div class="pic" style="--tone:#c9312b" role="img" aria-label="Occhiali protettivi a mascherina rossi e neri"></div><div class="name">Occhiali protettivi da lavoro a mascherina in PVC certificati CE, ...</div><div class="stars"></div><div class="price">€8,28</div></div>
  <div class="card"><div class="pic" style="--tone:#f4d21c" role="img" aria-label="Elmetto da lavoro giallo"></div><div class="name">Elmetto da lavoro antinfortunistico certificato EN 397,...</div><div class="stars"></div><div class="price">€7,67</div></div>
</div>

<div class="promo sale">
  <div class="k">ARMADI E ARREDO TECNICO</div>
  <div class="big">HUGE SALE</div>
  <div class="btn"><svg width="15" height="13" viewBox="0 0 16 14"><path d="M1 5h14l-2 8H3zM5 5l3-4 3 4" fill="#ffd600"/></svg>ACQUISTA ORA!</div>
  <div class="fifty">50</div>
  <div class="pc">%<br>OFF</div>
</div>
<div class="promo coll">
  <div class="pic" role="img" aria-label="Elmetto arancione, cuffie e guanti da lavoro"></div>
  <div class="k">AMAZING</div>
  <div class="big">COLLECTION</div>
  <div class="rule"></div>
  <div class="s">CHECK OUR DISCOUNTS</div>
</div>

<div class="sec-title" style="top:2786px">ARMADI E ARREDO TECNICO</div>
<div class="view-all" style="top:2781px">VIEW ALL</div>
<div class="products" style="top:2845px">
  <div class="card"><div class="pic" style="--tone:#c4c8cc" role="img" aria-label="Armadio in metallo grigio con ante aperte"></div><div class="name">Armadi in metallo multi uso, con ante battenti</div><div class="stars"></div><div class="price">€156,72</div></div>
  <div class="card"><div class="pic" style="--tone:#6b6c6e" role="img" aria-label="Baule da esterno in plastica aperto"></div><div class="name">Bauli da esterno in plastica, porta attrezzi per il giardino o per la casa</div><div class="stars"></div><div class="price">€21,81</div></div>
  <div class="card"><div class="pic" style="--tone:#4a4c50" role="img" aria-label="Armadio da esterno in plastica grigio scuro"></div><div class="name">Armadi da esterno in plastica, con ripiani regolabili, linea free...</div><div class="stars"></div><div class="price">€31,18</div></div>
  <div class="card"><div class="pic" style="--tone:#c9b79b" role="img" aria-label="Armadio da esterno in plastica beige con ripiani"></div><div class="name">Armadi da esterno in plastica, con ripiani integrati, linea steel...</div><div class="stars"></div><div class="price">€35,54</div></div>
  <div class="card"><div class="pic" style="--tone:#d8ceb9" role="img" aria-label="Armadio da esterno in plastica beige a due ante"></div><div class="name">Armadi da esterno in plastica, con ripiani regolabili, linea evolution</div><div class="stars"></div><div class="price">€51,68</div></div>
</div>

<div class="features">
  <div class="feat" style="left:0"><div class="ic"><svg width="40" height="30" viewBox="0 0 40 30" fill="none" stroke="#333" stroke-width="1.6"><rect x="2" y="5" width="22" height="16"/><path d="M24 10h8l6 6v5H24"/><circle cx="9" cy="24" r="3.5"/><circle cx="31" cy="24" r="3.5"/></svg></div><div><h4>Spedizioni<br>rapide</h4><p>Consegne In Tutta<br>Italia</p></div></div>
  <div class="feat" style="left:250px"><div class="ic"><svg width="36" height="36" viewBox="0 0 36 36" fill="none" stroke="#333" stroke-width="1.6"><path d="M6 20v-4a12 12 0 0 1 24 0v4"/><rect x="3" y="19" width="6" height="10" rx="2"/><rect x="27" y="19" width="6" height="10" rx="2"/><path d="M30 29c0 3-4 4-9 4"/></svg></div><div><h4>Servizio<br>clienti</h4><p>Dalle 9:00 Alle 13:00<br>02/55510420</p></div></div>
  <div class="feat" style="left:510px"><div class="ic"><svg width="32" height="36" viewBox="0 0 32 36" fill="none" stroke="#333" stroke-width="1.6"><rect x="4" y="2" width="24" height="32" rx="2"/><path d="M9 10h14M9 16h14M9 22h8"/><circle cx="22" cy="27" r="4"/></svg></div><div><h4>Prodotti<br>certificati</h4><p>Garantiti, di qualità e a<br>norma di legge</p></div></div>
  <div class="feat" style="left:788px"><div class="ic"><svg width="38" height="32" viewBox="0 0 38 32" fill="none" stroke="#333" stroke-width="1.6"><rect x="2" y="4" width="28" height="20" rx="2"/><path d="M2 10h28M6 18h8"/><path d="M28 16l7 3v5c0 4-3 6-7 7-4-1-7-3-7-7v-5z" fill="#fff"/></svg></div><div><h4>Pagamenti sicuri<br>Paywise,</h4><p>Carte di credito,<br>Bonifico, Contrassegno</p></div></div>
</div>

<div class="news">
  <div class="k">SUBSCRIBE</div>
  <div class="big">NEWSLETTER</div>
  <div class="s">By subscribing to our mailing list you will always be updated with the latest.</div>
  <div class="field"><svg width="16" height="12" viewBox="0 0 16 12"><rect x="0" y="0" width="16" height="12" rx="1" fill="#8a8f95"/><path d="M1 1l7 6 7-6" fill="none" stroke="#fff" stroke-width="1.2"/></svg>Enter your email address</div>
  <div class="btn">ISCRIVITI</div>
</div>

<div class="brand" style="left:88px;top:3735px;font-size:28px"><span class="mark" style="width:30px;height:30px"></span>CRATEVENDO</div>
<div class="social" style="left:124px"></div>
<div class="social" style="left:161px"></div>
<div class="social" style="left:198px"></div>
<div class="social" style="left:236px"></div>

<div class="foot-col" style="left:367px"><h5>CRATEVENDO SRL</h5><ul><li>Cratevendo Srl</li><li>Contatti</li><li>Chi Siamo</li><li>Certificazioni</li><li>Novità</li><li>Mappa del Sito</li></ul></div>
<div class="foot-col" style="left:579px"><h5>INFORMAZIONI</h5><ul><li>Info Privacy</li><li>Termini e Condizioni di<br>Vendita</li><li>Pagamenti</li><li>Spedizioni e Ritiri</li></ul></div>
<div class="foot-col" style="left:786px"><h5>SERVIZI</h5><ul><li>Preventivo Online</li><li>FAQ</li><li>Guide e Consigli</li><li>Cataloghi</li><li>Normative</li><li>Materiali</li></ul></div>
<div class="foot-col" style="left:956px"><h5>PAYMENT METHOD</h5></div>
<div class="paycard" style="left:956px;top:3720px;background:#3a3d42"></div>
<div class="paycard" style="left:1006px;top:3720px;background:#e9eef5"></div>
<div class="paycard" style="left:1056px;top:3720px;background:#eef0f6"></div>
<div class="paycard" style="left:956px;top:3757px;background:#f1f1f1"></div>
<div class="paycard" style="left:1006px;top:3757px;background:#2f7fce"></div>
<div class="paycard" style="left:1056px;top:3757px;background:#d6332f"></div>

<div class="copy-line"></div>
<div class="copy">CRATEVENDO SRL © 2021 ALL RIGHTS RESERVED</div>
<div class="totop"><svg width="14" height="16" viewBox="0 0 14 16"><path d="M7 15V2M2 7l5-5 5 5" fill="none" stroke="#222" stroke-width="1.6"/></svg></div>

</body>
</html>
```